New modern business card design

To design a brand new business card that's clean & modern in terms of layout.
I have attached our company logo and also basic information regarding what is needed on the card that also needs to be editable.

Target Market(s)

motor trade

Contact Information for Business Card

logo, name, title, tel, mob, email, address, www, all information is in the word.doc file

Requirements
Must have
• white background
Nice to have
• Nice clean font

```html
<!DOCTYPE html>
<html lang="en">
<head>
<meta charset="utf-8">
<title>Bolt Forge Ltd — Business Card</title>
<link href="https://fonts.googleapis.com/css2?family=Exo+2:wght@500;600&family=Roboto:wght@400;500&display=swap" rel="stylesheet">
<style>
  :root {
    --backdrop: #3a3b3e;
    --card: #ffffff;
    --brand-blue: #1688d6;
    --brand-blue-bright: #1a8fdc;
    --steel: #55585e;
    --steel-light: #c4c6c9;
    --ink: #2a2c30;
    --muted: #6b6e73;
    --on-blue: #ffffff;
  }
  * { box-sizing: border-box; margin: 0; padding: 0; }
  html, body { width: 799px; height: 1200px; overflow: hidden; }
  body {
    background: var(--backdrop);
    font-family: "Roboto", Arial, sans-serif;
    position: relative;
  }
  .card {
    position: absolute;
    left: 120px;
    width: 560px;
    height: 320px;
    background: var(--card);
    border-radius: 26px;
    overflow: hidden;
    box-shadow: 0 12px 30px rgba(0,0,0,0.35);
  }
  .card--front { top: 140px; }
  .card--back { top: 740px; }

  /* Front */
  .front-mark {
    position: absolute;
    top: 100px; left: 0; right: 0;
    display: flex; align-items: center; justify-content: center; gap: 14px;
  }
  .mark-square { width: 22px; height: 22px; background: var(--steel); }
  .front-mark .brand-name {
    font-family: "Exo 2", sans-serif;
    font-weight: 600;
    font-size: 38px;
    letter-spacing: 1px;
    color: var(--steel);
  }
  .front-rule {
    position: absolute; top: 165px; left: 150px; right: 150px;
    height: 1px; background: var(--steel); opacity: .5;
  }
  .front-web {
    position: absolute; bottom: 52px; left: 0; right: 0;
    display: flex; align-items: center; justify-content: center; gap: 18px;
    font-size: 17px; color: var(--ink);
  }
  .front-web .dash { width: 60px; height: 2px; background: var(--ink); }
  .front-web .accent { color: var(--brand-blue-bright); }

  /* Back */
  .back-mark {
    position: absolute; top: 74px; left: 36px;
    display: flex; align-items: center; gap: 10px;
  }
  .back-mark .mark-square { background: var(--brand-blue-bright); width: 18px; height: 18px; }
  .back-mark .brand-name {
    font-family: "Exo 2", sans-serif; font-weight: 600;
    font-size: 27px; color: var(--brand-blue-bright); letter-spacing: .5px;
  }
  .back-rule {
    position: absolute; top: 122px; left: 36px; width: 230px;
    height: 1px; background: var(--brand-blue-bright);
  }
  .contact {
    position: absolute; top: 64px; left: 300px; width: 240px;
    color: var(--ink);
  }
  .contact__name {
    font-family: "Exo 2", sans-serif; font-weight: 600;
    font-size: 27px; color: var(--brand-blue-bright);
  }
  .contact__title { font-size: 12px; color: var(--muted); margin-top: 2px; }
  .contact__address { font-size: 14px; line-height: 1.3; margin-top: 16px; }
  .contact__list { list-style: none; margin-top: 6px; font-size: 14px; line-height: 1.4; }
  .contact__list li { display: flex; align-items: center; gap: 10px; }
  .contact__list svg { width: 12px; height: 12px; fill: var(--brand-blue-bright); flex: none; }
  .back-footer { position: absolute; left: 0; bottom: 0; width: 560px; height: 90px; }
  .back-web {
    position: absolute; right: 70px; bottom: 40px;
    font-size: 15px; color: var(--on-blue);
  }
</style>
</head>
<body>

<section class="card card--front">
  <div class="front-mark">
    <span class="mark-square"></span>
    <span class="brand-name">BOLT FORGE LTD</span>
  </div>
  <div class="front-rule"></div>
  <div class="front-web">
    <span class="dash"></span>
    <span>www.<span class="accent">boltforge</span>.co.uk</span>
    <span class="dash"></span>
  </div>
</section>

<section class="card card--back">
  <div class="back-mark">
    <span class="mark-square"></span>
    <span class="brand-name">BOLT FORGE LTD</span>
  </div>
  <div class="back-rule"></div>

  <div class="contact">
    <p class="contact__name">Daniel Hughes</p>
    <p class="contact__title">General Manager</p>
    <p class="contact__address">Kestrel Road Denton,<br>Leeds LS9 4TQ</p>
    <ul class="contact__list">
      <li><svg viewBox="0 0 24 24"><path d="M6.6 10.8a15 15 0 0 0 6.6 6.6l2.2-2.2c.3-.3.7-.4 1-.2 1.1.4 2.3.6 3.6.6.6 0 1 .4 1 1V20c0 .6-.4 1-1 1A17 17 0 0 1 3 4c0-.6.4-1 1-1h3.5c.6 0 1 .4 1 1 0 1.3.2 2.5.6 3.6.1.3 0 .7-.2 1z"/></svg>0161 555 0182</li>
      <li><svg viewBox="0 0 24 24"><path d="M7 1h10a2 2 0 0 1 2 2v18a2 2 0 0 1-2 2H7a2 2 0 0 1-2-2V3a2 2 0 0 1 2-2zm0 3v14h10V4z"/></svg>07700 900 418</li>
      <li><svg viewBox="0 0 24 24"><path d="M2 5h20v14H2zm2 2v.5l8 5 8-5V7l-8 5z"/></svg>dhughes@boltforge.co.uk</li>
    </ul>
  </div>

  <svg class="back-footer" viewBox="0 0 560 90" aria-hidden="true">
    <rect x="0" y="70" width="560" height="20" fill="var(--steel-light)"/>
    <path d="M260 90 L290 30 Q296 20 310 20 L560 20 L560 90 Z" fill="var(--brand-blue)"/>
  </svg>
  <p class="back-web">www.boltforge.co.uk</p>
</section>

</body>
</html>
```